Business Card Design Project

I want a cleaner business card and envelope then what we have now, its too crowded.
Updates

I update with logo, this can be changed anyway you feel it looks best. I also have put gaurantee on there and extended time, this is my first time doing this. Also gave an example of current card

Target Market(s)

a wide array of customers from lattice 700 to small companies and cleints

Industry/Entity Type

Business

Requirements
Must have
• Need to have address, telephone number email
Nice to have
• a sharp professional card that stands out but is still very clean.
Should not have
• Not crazy looking

```html
<!DOCTYPE html>
<html lang="en">
<head>
<meta charset="utf-8">
<title>Harborcrest Insurance Group – Business Card</title>
<link href="https://fonts.googleapis.com/css2?family=Roboto+Condensed:wght@400;700&display=swap" rel="stylesheet">
<style>
  :root {
    --page-bg: #d9d6d1;
    --card-bg: #151515;
    --text-white: #f2f2f2;
    --text-grey: #8e8e8e;
    --rule-grey: #5a5a5a;
    --mark-silver: #a9a9a9;
  }
  * { box-sizing: border-box; margin: 0; padding: 0; }
  html, body {
    width: 1200px; height: 720px; overflow: hidden;
    background: var(--page-bg);
    font-family: "Roboto Condensed", "Arial Narrow", sans-serif;
  }
  .sheet {
    width: 1200px; height: 720px;
    display: flex; align-items: center; justify-content: center; gap: 40px;
  }
  .card {
    position: relative;
    width: 540px; height: 309px;
    background: var(--card-bg);
    color: var(--text-white);
    box-shadow: 0 10px 24px rgba(0,0,0,.25);
  }

  /* brand block */
  .brand { position: absolute; display: flex; flex-direction: column; align-items: center; }
  .brand-square { width: 44px; height: 44px; background: var(--mark-silver); margin-bottom: 8px; }
  .brand-name {
    color: var(--text-white); font-weight: 400; font-size: 13px;
    letter-spacing: 3px; text-transform: uppercase; text-align: center; line-height: 1.35;
  }

  /* front */
  .card-front .brand { left: 38px; top: 90px; width: 190px; }
  .divider { position: absolute; left: 252px; top: 48px; width: 1px; height: 212px; background: var(--rule-grey); }
  .contact { position: absolute; left: 272px; top: 48px; }
  .person-name { font-weight: 700; font-size: 25px; letter-spacing: .5px; text-transform: uppercase; line-height: 1; }
  .person-title { font-weight: 400; font-size: 22px; color: var(--text-grey); text-transform: uppercase; line-height: 1.1; margin-top: 2px; letter-spacing: .5px; }
  .contact-list { margin-top: 22px; display: grid; grid-template-columns: auto auto; column-gap: 6px; row-gap: 2px; font-size: 12.5px; }
  .contact-list dt { color: var(--text-grey); text-align: right; padding-right: 6px; border-right: 1px solid var(--rule-grey); }
  .contact-list dd { color: var(--text-white); }
  .contact-list .gap { margin-left: 14px; }

  /* back */
  .card-back .brand { left: 50%; top: 70px; transform: translateX(-50%); width: 240px; }
  .back-rule { position: absolute; top: 118px; height: 1px; background: var(--rule-grey); width: 130px; }
  .back-rule.left { left: 20px; }
  .back-rule.right { right: 20px; }
  .services {
    position: absolute; left: 0; right: 0; bottom: 32px; text-align: center;
    font-size: 10.5px; letter-spacing: 2.4px; text-transform: uppercase; color: var(--text-white);
  }
  .services span { color: var(--text-grey); margin: 0 6px; }
</style>
</head>
<body>
<main class="sheet">
  <section class="card card-front" aria-label="Business card front">
    <div class="brand">
      <div class="brand-square"></div>
      <div class="brand-name">Harborcrest<br>Insurance Group</div>
    </div>
    <div class="divider"></div>
    <div class="contact">
      <h1 class="person-name">Marla Quinn-Hester</h1>
      <p class="person-title">Operations Manager</p>
      <dl class="contact-list">
        <dt>phone</dt><dd>555-210-4400 ext 118</dd>
        <dt>direct</dt><dd>555-210-4407</dd>
        <dt>fax</dt><dd>555-317-2290</dd>
        <dt>email</dt><dd>mquinn-hester@harborcrestagency.com</dd>
        <dt>web</dt><dd>www.harborcrestagency.com</dd>
        <dt>address</dt><dd>18 Alder Point Rd.<br>Maple Ridge, MI 48000</dd>
      </dl>
    </div>
  </section>

  <section class="card card-back" aria-label="Business card back">
    <div class="back-rule left"></div>
    <div class="brand">
      <div class="brand-square"></div>
      <div class="brand-name">Harborcrest<br>Insurance Group</div>
    </div>
    <div class="back-rule right"></div>
    <p class="services">Commercial<span>|</span>Benefits<span>|</span>Financial Planning<span>|</span>Affluent Individuals</p>
  </section>
</main>
</body>
</html>
```